Magician | Speaker looks for an innovative business card design

I'm a magician and public speaker offering artistic and modern magical experiences.
I'm based in Brussels (Belgium.) I love magic performed up-close, creating a space of intimacy, even when I'm on stage.
The final design should communicate professionalism, elegance, artistry, and a friendly kind personality

I would like to see designs based either on my photos and/or the way I sign my name Remy Vok (see attached files for more info.)
Additional photos and more info about what I offer can be seen at www.remy-vok.net

My current business card design is also attached. I like the fact that the reverse of my current design includes quotes from master magicians about magic, changing the way my participants see the art of magic.

Note: I would like a double-sided card design. However, I need white space on the reverse to be able to write things on for my performances.

Details to include on the card:
Artist name: Remy Vok
Offer: magician + (public) speaker or magic + (public) speaking (the + sign can be replaced by another character, like a bullet or a pipe)
Phone: +32 471 265 903
Email: book@remy-vok.net
(optional) Website: www.remy-vok.net or remy-vok.net

Target Market(s)

Corporate, organisations, companies as well as individuals

Industry/Entity Type

Artists

Colors

Designer to choose colors to be used in the design.

Requirements
Nice to have
• A side with a mirror could be nice

```html
<!DOCTYPE html>
<html lang="en">
<head>
<meta charset="utf-8">
<title>Remy Vok – Business Card</title>
<link href="https://fonts.googleapis.com/css2?family=Open+Sans:wght@400&display=swap" rel="stylesheet">
<style>
  :root {
    --backdrop: #e9e6e2;
    --card-paper: #f7f4f2;
    --ink-brown: #4a2517;
    --ink-dark: #1e1a18;
    --portrait-dark: #1a1614;
    --portrait-brick: #5a3426;
    --portrait-warm: #7a4a36;
  }
  html, body {
    margin: 0;
    padding: 0;
    width: 1200px;
    height: 900px;
    overflow: hidden;
    background: var(--backdrop);
    font-family: "Open Sans", Arial, sans-serif;
  }
  .business-card {
    position: absolute;
    left: 120px;
    top: 153px;
    width: 960px;
    height: 594px;
    display: flex;
    box-shadow: 0 10px 30px rgba(0,0,0,0.18);
  }
  .portrait {
    width: 456px;
    height: 100%;
    background:
      radial-gradient(ellipse at 50% 35%, var(--portrait-warm) 0%, transparent 55%),
      linear-gradient(180deg, var(--portrait-brick) 0%, var(--portrait-dark) 75%);
  }
  .info-panel {
    position: relative;
    flex: 1;
    background: var(--card-paper);
  }
  .brand {
    position: absolute;
    left: 38px;
    top: 60px;
  }
  .brand-name {
    margin: 0;
    font-size: 58px;
    font-weight: 400;
    color: var(--ink-brown);
    line-height: 1;
    padding-left: 70px;
  }
  .brand-rule {
    display: block;
    margin-top: 14px;
  }
  .tagline {
    position: absolute;
    left: 42px;
    top: 190px;
    margin: 0;
    font-size: 24px;
    color: var(--ink-dark);
  }
  .contact-list {
    position: absolute;
    left: 48px;
    top: 445px;
    margin: 0;
    padding: 0;
    list-style: none;
    font-size: 23px;
    line-height: 35px;
    color: var(--ink-dark);
  }
</style>
</head>
<body>
  <div class="business-card">
    <div class="portrait" role="img" aria-label="Portrait photo of the magician seated in a dark blazer in front of a brick wall"></div>
    <div class="info-panel">
      <div class="brand">
        <h1 class="brand-name">Remy Vok</h1>
        <svg class="brand-rule" width="370" height="24" viewBox="0 0 370 24" aria-hidden="true">
          <path d="M2 20 C 90 4, 240 2, 366 14" fill="none" stroke="var(--ink-brown)" stroke-width="3" stroke-linecap="round"/>
        </svg>
      </div>
      <p class="tagline">Magician &amp; Public Speaker</p>
      <ul class="contact-list">
        <li>+32 471 265 903</li>
        <li>book@remy-vok.net</li>
        <li>www.remy-vok.net</li>
      </ul>
    </div>
  </div>
</body>
</html>
```